Regional Showdown Flyer for Holiday Program

Need a one page flyer, can be back to front or one page, ensuring you can fit all information, colourful, aimed at a market of 8-13 year old boys and girls.
The flyer needs to be noticed, needs to have certain information on it and needs to be Autralian Rule Football orientated.
Have uploaded file so you can understand the style (not content), style of flyer I am looking at getting submitted.

Target Market(s)

8-13 year old boys and girls and their parents.

Requirements
Must have
• Regional Showdown Event
• Price for Regional Showdown Day will be $85
• Strictly Limited Places, only the best footballers should enter this challenge
• Inaugural event, be the first Regional Showdown Winner for your age!
• Do you love a challenge! Put yourself to the test!
• Are you up to it - Water Slide Goal Kicking Contest! The fastest kick in the West (tested by our very own speed gun)! Can you survive the Footy Titan Trail or Last One Standing Goal Kicking! These challenges are crazy are super fun!
• If you think you can deliver on the big stage then this is for YOU!
• All District age winners will receive prizes, awards and the adulation from all their peers!
• Year's 3-5 from 9am to 12pm
• Year's 6-8 from 1-4pm
• All challengers compete against their own age
• Lunch Provided
• Monday 16th April - Upper Tarrowby Regional Showdown Day at Tarrowby Oval
• Tuesday 17th April - North Tarrowby Regional Showdown Day at Kilmorna Reserve
• Wednesday 18th April - Yarlo Regional Showdown Day - Dunhaven Football Club
• Every Challenge Participant receives a District Football!
• Need to put all 3 District Football Logos on the bottom of the flyer, logos attached at bottom.
Nice to have
• Plenty of colour, if you can fit all information on one page that would be fine
Should not have
• Dull, boring, any footballs should be Aussie Rules footballs not NFL or soccer

```html
<!DOCTYPE html>
<html lang="en">
<head>
<meta charset="utf-8">
<title>Regional Showdown Event</title>
<link rel="stylesheet" href="https://fonts.googleapis.com/css2?family=Bowlby+One&family=Titan+One&family=Open+Sans:ital,wght@0,700;0,800;1,700&display=swap">
<style>
:root{
  --navy:#102a6b;
  --navy-deep:#0b1d4d;
  --red:#e3261f;
  --red-deep:#a5141a;
  --blue:#1d4fc4;
  --yellow:#ffe500;
  --green:#1f7a3a;
  --ink:#111;
  --white:#fff;
  --pink:#ff3f9b;
  --cyan:#35c7f0;
  --orange:#ff8a1e;
}
*{box-sizing:border-box;margin:0;padding:0}
html,body{width:800px;height:1200px;overflow:hidden;background:var(--white)}
.flyer{position:relative;width:800px;height:1200px;background:var(--white)}
.artboard{position:absolute;left:22px;top:22px;width:758px;height:1168px;overflow:hidden;
  background:
   radial-gradient(ellipse 320px 260px at 400px 260px,#e9f4ff 0,rgba(233,244,255,0) 100%),
   radial-gradient(ellipse 300px 300px at 80px 300px,var(--pink) 0,rgba(255,63,155,0) 100%),
   radial-gradient(ellipse 300px 300px at 720px 330px,var(--cyan) 0,rgba(53,199,240,0) 100%),
   radial-gradient(ellipse 400px 300px at 700px 900px,var(--orange) 0,rgba(255,138,30,0) 100%),
   radial-gradient(ellipse 400px 300px at 100px 1000px,#b03cf0 0,rgba(176,60,240,0) 100%),
   linear-gradient(180deg,#ff4fa0 0%,#c86bff 30%,#ffd1e6 45%,#ff6aa8 70%,#ffb13b 100%)}
.artboard::after{content:"";position:absolute;left:0;right:0;bottom:0;height:24px;background:var(--ink)}
.top-edge{position:absolute;left:0;top:0;width:100%;height:6px;background:#2a1b4a}

.title{position:absolute;left:0;top:36px;width:100%;text-align:center;font-family:"Bowlby One",sans-serif;
  color:var(--white);font-size:100px;line-height:104px;letter-spacing:1px;
  -webkit-text-stroke:4px var(--navy-deep);paint-order:stroke fill;
  text-shadow:5px 5px 0 #3a63e0,-4px -4px 0 #ff5fb0,0 8px 14px rgba(0,0,0,.35)}
.event{position:absolute;left:0;top:280px;width:100%;text-align:center;font-family:"Bowlby One",sans-serif;
  font-size:90px;line-height:100px;transform:skewX(-8deg);
  -webkit-text-stroke:4px var(--white);paint-order:stroke fill;text-shadow:4px 5px 0 rgba(0,0,0,.35)}
.event .e{color:var(--blue);font-size:112px}
.event .rest{color:var(--red)}

.intro{position:absolute;left:0;top:404px;width:100%;text-align:center;font-family:"Titan One",sans-serif;
  font-size:23px;line-height:30px;color:var(--ink);-webkit-text-stroke:5px var(--white);paint-order:stroke fill}
.intro .tagline{display:block;margin-top:10px;font-size:24px}
.tagline .green{color:var(--green)}
.tagline .red{color:var(--red)}
.tagline .blue{color:var(--navy)}

.banner{position:absolute;font-family:"Titan One",sans-serif;color:var(--white)}
.banner-price{left:350px;top:522px;width:408px;height:80px;background:var(--navy);transform:rotate(-3deg);
  border-top:4px solid var(--white);border-bottom:4px solid var(--white);
  display:flex;align-items:center;justify-content:flex-start;gap:12px;padding:0 14px 0 34px}
.banner-price p{font-size:20px;line-height:22px;transform:skewX(-10deg);white-space:nowrap}
.banner-price .amount{font-size:46px;line-height:50px;color:var(--yellow);transform:skewX(-10deg);
  -webkit-text-stroke:2px var(--navy-deep);paint-order:stroke fill}
.banner-limited{left:340px;top:634px;width:430px;height:86px;background:var(--red-deep);transform:rotate(-4deg);
  border-top:4px solid var(--white);border-bottom:4px solid var(--white);padding:12px 20px 0 36px;text-align:center}
.banner-limited p{font-size:18px;line-height:20px;transform:skewX(-10deg)}

.football{position:absolute;left:28px;top:590px;width:460px;height:320px;border-radius:50%;transform:rotate(-22deg);
  background:radial-gradient(ellipse at 35% 30%,#ff8b7a 0,#f0301e 35%,#c4170f 75%,#8a0d08 100%);
  box-shadow:8px 14px 24px rgba(0,0,0,.35)}

.features{position:absolute;left:486px;top:735px;width:272px;height:333px;background:var(--navy);border:2px solid var(--white);
  list-style:none;padding:16px 10px 0 22px;font-family:"Open Sans",sans-serif;font-weight:700;color:var(--white);
  font-size:11.6px;line-height:15px}
.features li{position:relative;margin-bottom:14px}
.features .tick{position:absolute;left:-50px;top:-8px;width:42px;height:42px}
.features .times{font-size:14.5px;line-height:17px}
.features .note{display:block;font-style:italic;font-size:10.4px;line-height:13px}
.features .lunch{font-size:15px;line-height:18px;margin-top:4px}

.dates{position:absolute;left:14px;top:930px;width:406px;height:152px;background:var(--navy);border:2px solid var(--white);
  list-style:none;padding:12px 12px 0 30px;font-family:"Open Sans",sans-serif;font-weight:700;color:var(--white);
  font-size:12.2px;line-height:17px;text-align:center}
.dates li{position:relative}
.dates li::before{content:"";position:absolute;left:-14px;top:4px;width:9px;height:9px;border-radius:50%;background:var(--yellow)}

.partners{position:absolute;left:168px;top:1076px;width:420px;height:80px;background:var(--white);border-radius:12px;
  display:flex;align-items:center;justify-content:space-around;padding:0 14px;box-shadow:0 2px 6px rgba(0,0,0,.25)}
.partner{display:flex;align-items:center;gap:6px;font-family:"Open Sans",sans-serif;font-weight:800;font-size:12px;line-height:14px;color:var(--navy)}
.partner .mark{width:14px;height:14px;border-radius:50%;background:var(--navy);flex:none}
</style>
</head>
<body>
<div class="flyer">
  <div class="artboard" role="img" aria-label="Bright multicolour paint splash background">
    <div class="top-edge"></div>

    <h1 class="title">REGIONAL<br>SHOWDOWN</h1>
    <div class="event"><span class="e">E</span><span class="rest">VENT</span></div>

    <div class="intro">
      INAUGURAL EVENT, BE THE FIRST REGIONAL<br>SHOWDOWN WINNER FOR YOUR AGE!
      <span class="tagline"><span class="green">DO YOU LOVE A </span><span class="red">CHALLENGE!</span><span class="blue"> PUT YOURSELF TO THE TEST!</span></span>
    </div>

    <div class="football" role="img" aria-label="Red Australian Rules football"></div>

    <div class="banner banner-price">
      <p>Price for Regional<br>Showdown Day will be</p>
      <span class="amount">$85</span>
    </div>
    <div class="banner banner-limited">
      <p>Strictly Limited Places, only<br>the best footballers<br>should enter this challenge</p>
    </div>

    <ul class="dates">
      <li>Monday 16th April - Upper Tarrowby Regional Showdown Day at Tarrowby Oval</li>
      <li>Tuesday 17th April - North Tarrowby Regional Showdown Day at Kilmorna Reserve</li>
      <li>Wednesday 18th April - Yarlo Regional Showdown Day Dunhaven Football Club</li>
      <li>Every Challenge Participant receives a District Football!</li>
    </ul>

    <ul class="features">
      <li><svg class="tick" viewBox="0 0 44 44"><circle cx="20" cy="24" r="16" fill="#ffe500"/><path d="M10 22l8 9L40 6" fill="none" stroke="#111" stroke-width="5" stroke-linecap="round" stroke-linejoin="round"/></svg>Are you up to it - Water Slide Goal Kicking Contest! The fastest kick in the West (tested by our very own speed gun)! Can you survive the Footy Titan Trail or Last One Standing Goal Kicking! These challenges are crazy are super fun!</li>
      <li><svg class="tick" viewBox="0 0 44 44"><circle cx="20" cy="24" r="16" fill="#ffe500"/><path d="M10 22l8 9L40 6" fill="none" stroke="#111" stroke-width="5" stroke-linecap="round" stroke-linejoin="round"/></svg>If you think you can deliver on the big stage then this is for YOU!</li>
      <li><svg class="tick" viewBox="0 0 44 44"><circle cx="20" cy="24" r="16" fill="#ffe500"/><path d="M10 22l8 9L40 6" fill="none" stroke="#111" stroke-width="5" stroke-linecap="round" stroke-linejoin="round"/></svg>All District age winners will receive prizes, awards and the adulation from all their peers!</li>
      <li><svg class="tick" viewBox="0 0 44 44"><circle cx="20" cy="24" r="16" fill="#ffe500"/><path d="M10 22l8 9L40 6" fill="none" stroke="#111" stroke-width="5" stroke-linecap="round" stroke-linejoin="round"/></svg><span class="times">Year's 3-5 from 9am to 12pm<br>Year's 6-8 from 1-4pm</span><span class="note">All challengers compete against their own age</span></li>
      <li class="lunch"><svg class="tick" viewBox="0 0 44 44"><circle cx="20" cy="24" r="16" fill="#ffe500"/><path d="M10 22l8 9L40 6" fill="none" stroke="#111" stroke-width="5" stroke-linecap="round" stroke-linejoin="round"/></svg>Lunch Provided</li>
    </ul>

    <div class="partners">
      <div class="partner"><span class="mark"></span><span>Reefrunners<br>District</span></div>
      <div class="partner"><span class="mark"></span><span>Ironbarks<br>District</span></div>
      <div class="partner"><span class="mark"></span><span>Yarlo<br>District</span></div>
    </div>
  </div>
</div>
</body>
</html>
```